Business card design needed

We are a wine business involved in winemaking, broking and packaging on behalf of clients globally with the majority being Asian. The design should be quite traditional and classic with some red used, font used should be easily read.

Target Market(s)

Trade customers other business owners

Industry/Entity Type

Business

Contact Information for Business Card

Rosalind Whitcombe
Meridale Wine Collective
PO Box 738, Fenwick Vale
South Australia 5041
Phone: +61 (0)487 263 918
Email: mvcellar@brindlenet.com.au

Logo styles of interest
Lettermark Logo

```html
<!DOCTYPE html>
<html lang="en">
<head>
<meta charset="utf-8">
<title>Rosalind Whitcombe — Business Card</title>
<link rel="stylesheet" href="https://fonts.googleapis.com/css2?family=Poiret+One&display=swap">
<style>
  :root {
    --card-red: #640000;
    --ink-white: #ffffff;
    --art-white: #ffffff;
  }
  html, body {
    margin: 0;
    padding: 0;
    width: 1200px;
    height: 741px;
    overflow: hidden;
    background: var(--card-red);
  }
  .card {
    position: relative;
    width: 1200px;
    height: 741px;
    background: var(--card-red);
    color: var(--ink-white);
    font-family: "Poiret One", sans-serif;
    overflow: hidden;
  }
  .wine-art {
    position: absolute;
    left: 0;
    top: 63px;
    width: 303px;
    height: 678px;
  }
  .line {
    position: absolute;
    right: 45px;
    margin: 0;
    line-height: 1;
    white-space: nowrap;
    text-align: right;
    font-weight: 400;
  }
  .holder-name {
    top: 82px;
    font-size: 66px;
    letter-spacing: 0.09em;
  }
  .company-tagline {
    top: 158px;
    font-size: 42px;
    letter-spacing: 0.1em;
  }
  .address-line {
    font-size: 40px;
    letter-spacing: 0.12em;
  }
  .address-line.first { top: 481px; }
  .address-line.second { top: 534px; }
  .contact-line {
    font-size: 34px;
    letter-spacing: 0.12em;
  }
  .contact-line.phone { top: 609px; }
  .contact-line.email { top: 654px; }
</style>
</head>
<body>
  <main class="card">
    <svg class="wine-art" viewBox="0 0 303 678" role="img" aria-label="White silhouette of a wine bottle with a wine glass in front of it">
      <rect x="0" y="0" width="303" height="678" fill="var(--art-white)"/>
    </svg>

    <h1 class="line holder-name">Rosalind Whitcombe</h1>
    <p class="line company-tagline">Meridale Wine</p>

    <p class="line address-line first">Collective PO Box 738</p>
    <p class="line address-line second">Fenwick Vale South Australia 5041</p>

    <p class="line contact-line phone">Phone: +61 (0)487 263 918</p>
    <p class="line contact-line email">Email: mvcellar@brindlenet.com.au</p>
  </main>
</body>
</html>
```